Consulting Company needs business card design

We need a business card design for a new consulting and business solutions company based in Bermuda called Corvale Partners Limited. Looking for a double sided business card with one side only including the company logo thats attached and the other including contact information. Logo contains blue and turquoise colors and is fine to be on both sides of the card.
Contact Information for Business Card
Corvale Partners Limited
P.O. Box HM318
Devonshire DV BX
Bermuda
Name: Marcus Pellegrin
Position: Director
Telephone: 1 441 733 4906
Email: mpellegrin@corvale.example
Website: www.corvale.example

```html
<!DOCTYPE html>
<html lang="en">
<head>
<meta charset="utf-8">
<title>Corvale Partners Limited – Business Card</title>
<link href="https://fonts.googleapis.com/css2?family=Arimo:wght@400;700&display=swap" rel="stylesheet">
<style>
  :root {
    --backdrop: #2a2a2c;
    --card-black: #030303;
    --card-white: #ffffff;
    --brand-blue: #1e90d8;
    --brand-teal: #17b3ae;
    --text-blue: #1a8fd3;
    --text-teal: #16a9a8;
  }
  * { margin: 0; padding: 0; box-sizing: border-box; }
  html, body { width: 1200px; height: 880px; overflow: hidden; }
  body {
    background: var(--backdrop);
    font-family: "Arimo", Arial, sans-serif;
    position: relative;
  }
  .card {
    position: absolute;
    width: 560px;
    height: 320px;
    border-radius: 22px;
    overflow: hidden;
    box-shadow: 0 14px 30px rgba(0,0,0,0.45);
  }
  .card--front {
    left: 70px; top: 70px;
    background: var(--card-black);
    display: flex; align-items: center; justify-content: center;
  }
  .card--back {
    left: 570px; top: 490px;
    background: var(--card-white);
  }
  .brand-name {
    display: flex; align-items: center; gap: 14px;
    color: var(--brand-blue);
    font-weight: 700;
    letter-spacing: 1px;
    text-transform: uppercase;
    white-space: nowrap;
  }
  .brand-name__dot {
    width: 22px; height: 22px; border-radius: 50%;
    background: var(--brand-teal);
    flex: none;
  }
  .card--front .brand-name { font-size: 30px; }
  .back__top {
    position: absolute; left: 0; top: 0; width: 100%; height: 172px;
    background: var(--card-black);
  }
  .back__stripe {
    position: absolute; left: 0; top: 172px; width: 100%; height: 8px;
    background: linear-gradient(90deg, var(--brand-blue), var(--brand-teal));
  }
  .back__tab {
    position: absolute; left: -16px; top: 114px;
    width: 32px; height: 32px; border-radius: 50%;
    background: var(--brand-teal);
  }
  .card--back .brand-name {
    position: absolute; right: 30px; top: 34px;
    font-size: 22px;
  }
  .holder {
    position: absolute; left: 34px; top: 110px;
    color: var(--text-blue);
  }
  .holder__name { font-size: 19px; font-weight: 700; text-transform: uppercase; letter-spacing: 0.5px; }
  .holder__role { font-size: 14px; }
  .contact {
    position: absolute; left: 48px; top: 194px;
    color: var(--text-blue);
    font-size: 12px; line-height: 1.25;
  }
  .contact__company { color: var(--text-teal); font-weight: 700; font-size: 16px; }
  .contact__lines { list-style: none; margin-top: 4px; }
  .contact__lines li { display: flex; align-items: center; gap: 8px; margin-top: 2px; height: 16px; }
  .contact__icon { width: 16px; height: 16px; flex: none; }
  .contact strong { font-weight: 700; }
</style>
</head>
<body>

  <section class="card card--front" aria-label="Card front">
    <div class="brand-name"><span class="brand-name__dot"></span>Corvale Partners Limited</div>
  </section>

  <section class="card card--back" aria-label="Card back">
    <div class="back__top"></div>
    <div class="back__stripe"></div>
    <div class="back__tab"></div>
    <div class="brand-name">Corvale Partners Limited</div>

    <div class="holder">
      <div class="holder__name">Marcus Pellegrin</div>
      <div class="holder__role">Director</div>
    </div>

    <div class="contact">
      <div class="contact__company">Corvale Partners Limited</div>
      <div>P.O. Box HM318</div>
      <div>Westmoor WM 22, Northisle</div>
      <ul class="contact__lines">
        <li>
          <svg class="contact__icon" viewBox="0 0 16 16" aria-hidden="true"><circle cx="8" cy="8" r="7.5" fill="var(--brand-teal)"/><path d="M5 4.5c-.6.4-.8 1.2-.5 2 .8 2.2 2.7 4.2 5 5 .8.3 1.6.1 2-.5l-1.6-1.4-1 .6c-1-.5-1.9-1.4-2.4-2.4l.6-1z" fill="#fff"/></svg>
          1 441 733 4906
        </li>
        <li>
          <svg class="contact__icon" viewBox="0 0 16 16" aria-hidden="true"><circle cx="8" cy="8" r="7.5" fill="var(--brand-teal)"/><rect x="4" y="5.2" width="8" height="5.6" fill="#fff"/><path d="M4 5.2l4 3 4-3" stroke="var(--brand-teal)" stroke-width="0.9" fill="none"/></svg>
          mpellegrin@corvale.example
        </li>
        <li>
          <svg class="contact__icon" viewBox="0 0 16 16" aria-hidden="true"><circle cx="8" cy="8" r="7.5" fill="var(--brand-teal)"/><circle cx="8" cy="8" r="4" fill="none" stroke="#fff" stroke-width="1"/><ellipse cx="8" cy="8" rx="1.8" ry="4" fill="none" stroke="#fff" stroke-width="0.9"/><path d="M4 8h8" stroke="#fff" stroke-width="0.9"/></svg>
          <span>www.<strong>corvale</strong>.example</span>
        </li>
      </ul>
    </div>
  </section>

</body>
</html>
```